Law Office needs stationery design and business card

I currently have been using the same letterhead for the last 8 years. Since i 'm about to adding another location, I want to revamp my letterhead and business card. I already have a logo i'm happy with. I will upload my current letterhead, fax sheet, envelope, and logos. I need a business card also. I have 2 locations, 1 phone number, 1 fax line, website, etc. If possible and fitting with the design, I would like to keep the same information listed currently on the letterhead.

**Keep in mind, I also NEED A FAX SHEET COVER. thank you

Hello, Please submit a Gray Scale or Black and White version of your designs also, since most of the time I will be printing NON color stationery. I will seldom use a color print for my letterhead, I would like to have a color version for my benefit, however i will print in grayscale majority of the time . For the Business Card, that can just be in color. When I get my business cards they will be in color.Thank youEnrique Added Sunday, September 18, 2016

```html
<!DOCTYPE html>
<html lang="en">
<head>
<meta charset="utf-8">
<title>Quenbrook Law – Business Card</title>
<link rel="stylesheet" href="https://fonts.googleapis.com/css2?family=Source+Sans+3:ital,wght@0,400;0,600;1,400&display=swap">
<style>
  :root {
    --backdrop: #9c9c9c;
    --card-light: #f1f1f0;
    --card-dark: #1f1b18;
    --gold: #a88c56;
    --ink: #2a2522;
    --text: #4d4d4d;
    --white: #f4f4f2;
    --faint: rgba(205, 205, 202, 0.4);
  }
  * { box-sizing: border-box; margin: 0; padding: 0; }
  html, body {
    width: 1105px; height: 1200px; overflow: hidden;
    background: var(--backdrop);
    font-family: "Source Sans 3", "Myriad Pro", Arial, sans-serif;
  }
  .canvas { position: relative; width: 1105px; height: 1200px; }
  .card {
    position: absolute; left: 182px; width: 746px; height: 427px; overflow: hidden;
  }
  .card--front { top: 119px; background: var(--card-light); }
  .card--back { top: 637px; background: var(--card-dark); }

  .watermark-square {
    position: absolute; left: 40px; top: 40px; width: 330px; height: 330px;
    background: var(--faint); transform: rotate(-14deg);
  }
  .holder { position: absolute; left: 47px; top: 52px; }
  .holder__name { color: var(--gold); font-size: 24px; font-weight: 600; line-height: 30px; }
  .holder__title { color: var(--ink); font-size: 19px; line-height: 24px; }

  .addresses {
    position: absolute; left: 47px; top: 131px;
    color: var(--text); font-size: 18.5px; line-height: 27.5px; font-style: normal;
  }

  .contacts { position: absolute; left: 47px; top: 255px; list-style: none; color: var(--text); font-size: 18.5px; }
  .contacts li { display: flex; align-items: center; height: 28.6px; }
  .contacts svg { width: 17px; height: 17px; margin-right: 13px; fill: var(--gold); flex: none; }

  .brand-front { position: absolute; left: 375px; top: 225px; width: 320px; text-align: center; }
  .brand-front__mark { display: block; width: 76px; height: 76px; margin: 0 auto 34px; background: var(--gold); }
  .brand-front__name { color: var(--ink); font-size: 28px; font-weight: 600; letter-spacing: 2px; line-height: 36px; }

  .brand-back { position: absolute; left: 0; top: 112px; width: 100%; text-align: center; }
  .brand-back__mark { display: block; width: 120px; height: 120px; margin: 0 auto 24px; background: var(--gold); }
  .brand-back__name { color: var(--white); font-size: 26px; font-weight: 600; letter-spacing: 2px; line-height: 34px; }

  .social {
    position: absolute; left: 0; top: 358px; width: 100%;
    display: flex; justify-content: center; align-items: center;
    color: var(--white); font-size: 19px; font-style: italic;
  }
  .social__square { width: 15px; height: 15px; background: var(--gold); margin-right: 9px; }
</style>
</head>
<body>
<main class="canvas">
  <section class="card card--front">
    <div class="watermark-square"></div>
    <div class="holder">
      <p class="holder__name">Gustavo Quenbrook Esq.</p>
      <p class="holder__title">Attorney</p>
    </div>
    <address class="addresses">
      418 East Harbor St.<br>
      Suite 210, Fairview, PA 19070<br>
      627 Linden Ave.<br>
      Brookfield, PA 19022
    </address>
    <ul class="contacts">
      <li><svg viewBox="0 0 24 24"><path d="M6.6 10.8a15 15 0 0 0 6.6 6.6l2.2-2.2a1 1 0 0 1 1-.25 11.4 11.4 0 0 0 3.6.57 1 1 0 0 1 1 1V20a1 1 0 0 1-1 1A17 17 0 0 1 3 4a1 1 0 0 1 1-1h3.5a1 1 0 0 1 1 1c0 1.25.2 2.45.57 3.57a1 1 0 0 1-.25 1z"/></svg>555.201.4830</li>
      <li><svg viewBox="0 0 24 24"><path d="M7 1h10a2 2 0 0 1 2 2v18a2 2 0 0 1-2 2H7a2 2 0 0 1-2-2V3a2 2 0 0 1 2-2zm0 3v14h10V4zm5 15.5a1.2 1.2 0 1 0 0 2.4 1.2 1.2 0 0 0 0-2.4z"/></svg>555.307.2164</li>
      <li><svg viewBox="0 0 24 24"><path d="M2 5h20v14H2zm2 2v.4l8 5 8-5V7zm0 2.8V17h16V9.8l-8 5z"/></svg>Gustavo@QuenbrookLaw.com</li>
      <li><svg viewBox="0 0 24 24"><path d="M12 2a10 10 0 1 0 0 20 10 10 0 0 0 0-20zm-1 17.9A8 8 0 0 1 4.2 10.5L9 15v1a2 2 0 0 0 2 2zm6.9-2.5A2 2 0 0 0 16 16h-1v-3a1 1 0 0 0-1-1H8v-2h2a1 1 0 0 0 1-1V7h2a2 2 0 0 0 2-2v-.4a8 8 0 0 1 2.9 12.8z"/></svg>www.QuenbrookLaw.com</li>
    </ul>
    <div class="brand-front">
      <span class="brand-front__mark"></span>
      <p class="brand-front__name">QUENBROOK LAW</p>
    </div>
  </section>

  <section class="card card--back">
    <div class="brand-back">
      <span class="brand-back__mark"></span>
      <p class="brand-back__name">QUENBROOK LAW</p>
    </div>
    <p class="social"><span class="social__square"></span>QuenbrookLaw</p>
  </section>
</main>
</body>
</html>
```